TRESSLY FACEBOOK DESIGN

I need new design for facebook https://www.facebook.com/tresslyitalia.
Our Businnes is Hair care , hair replacement , hair transplant . hair regrowth . i NEED MEDICAL AND PROFESSIONAL DESIGN. I NEED ALSO RESPONSIVE DESIGN

Target Market(s)

Consumers

Industry/Entity Type

MEDICAL AND COSMETICS

Colors
0054AA
0677BA
7BADD7
CADEEF
E8F1F8

Requirements
Must have
• MEDICAL
Nice to have
• RESPONSIVE DESIGN

```html
<!DOCTYPE html>
<html lang="it">
<head>
<meta charset="utf-8">
<title>Tressly – Facebook Cover</title>
<link rel="stylesheet" href="https://fonts.googleapis.com/css2?family=Roboto:wght@400;700&family=Caveat+Brush&display=swap">
<style>
  :root {
    --stage: #262626;
    --navy: #2a3f9e;
    --arc-blue: #1f4fa8;
    --brand-blue: #0054aa;
    --mid-blue: #0677ba;
    --sky-blue: #3aa0e0;
    --soft-blue: #7badd7;
    --pale-blue: #cadeef;
    --mist: #e8f1f8;
    --tag-blue: #7ec3f0;
    --white: #ffffff;
  }
  * { margin: 0; padding: 0; box-sizing: border-box; }
  html, body {
    width: 1200px;
    height: 802px;
    overflow: hidden;
    background: var(--stage);
  }
  .cover {
    position: absolute;
    left: 47px;
    top: 209px;
    width: 1098px;
    height: 417px;
    display: block;
  }
  .brand-name {
    font-family: "Roboto", sans-serif;
    font-weight: 700;
    fill: var(--brand-blue);
  }
  .tagline {
    font-family: "Roboto", sans-serif;
    font-weight: 400;
    fill: var(--mid-blue);
    letter-spacing: 1px;
  }
  .hashtag {
    font-family: "Roboto", sans-serif;
    font-weight: 700;
    fill: var(--tag-blue);
  }
  .headline {
    font-family: "Caveat Brush", cursive;
    fill: var(--sky-blue);
  }
  .headline .hash { fill: var(--arc-blue); }
</style>
</head>
<body>
<svg class="cover" viewBox="0 0 1342 510" xmlns="http://www.w3.org/2000/svg">
  <defs>
    <linearGradient id="bg-fade" x1="0" y1="0" x2="0.3" y2="1">
      <stop offset="0" stop-color="#ffffff"/>
      <stop offset="0.55" stop-color="#f2f8fc"/>
      <stop offset="1" stop-color="#9fd0f0"/>
    </linearGradient>
    <linearGradient id="left-photo" x1="0" y1="0" x2="1" y2="1">
      <stop offset="0" stop-color="#4fa9dd"/>
      <stop offset="0.6" stop-color="#e9c8c0"/>
      <stop offset="1" stop-color="#7cc2ea"/>
    </linearGradient>
    <linearGradient id="right-photo" x1="0" y1="0" x2="0" y2="1">
      <stop offset="0" stop-color="#e3c39c"/>
      <stop offset="0.6" stop-color="#f1dccb"/>
      <stop offset="1" stop-color="#eef0f4"/>
    </linearGradient>
  </defs>

  <rect class="cover-bg" width="1342" height="510" fill="url(#bg-fade)"/>

  <path class="photo-left" role="img" aria-label="Foto: ragazza preoccupata con una spazzola piena di capelli caduti"
        d="M0 0 H362 Q470 200 338 412 H0 Z" fill="url(#left-photo)"/>
  <path class="photo-arc" d="M362 0 H397 Q505 205 352 420 L330 412 Q470 200 362 0 Z" fill="var(--arc-blue)"/>

  <rect class="photo-right" role="img" aria-label="Foto: donna sorridente con capelli biondi ondulati che fa il segno OK"
        x="840" y="108" width="480" height="380" rx="24" fill="url(#right-photo)"/>

  <path class="wave" d="M0 422 Q200 405 400 412 Q620 425 842 482 Q1120 465 1342 385 V510 H0 Z" fill="var(--navy)"/>

  <circle class="brand-mark" role="img" aria-label="Spazio simbolo del marchio" cx="645" cy="168" r="92" fill="var(--sky-blue)"/>
  <text class="brand-name" x="632" y="352" font-size="62" text-anchor="middle">TRESSLY</text>
  <text class="tagline" x="632" y="384" font-size="17" text-anchor="middle" textLength="310" lengthAdjust="spacing">CURA E REINTEGRAZIONE DEI CAPELLI</text>
  <path class="brand-swoosh" d="M457 425 Q640 440 822 405" fill="none" stroke="var(--sky-blue)" stroke-width="2.5" stroke-linecap="round"/>

  <text class="headline" x="877" y="82" font-size="66" textLength="430" lengthAdjust="spacingAndGlyphs"><tspan class="hash">#</tspan>WORRYFREE</text>

  <text class="hashtag" x="210" y="457" font-size="20" text-anchor="middle">#CAPELLIFELICI</text>
  <text class="hashtag" x="210" y="487" font-size="20" text-anchor="middle" textLength="296" lengthAdjust="spacingAndGlyphs">#SEMPLICEMENTEMIGLIORI</text>
</svg>
</body>
</html>
```